Brindle Structures Construction Company Seeking Modern Website

We are a small construction company wanting to create a web presence. We don't have much in the way of current content but will get photos as they come in. Attached is a picture of our business card.
The pages we would like on the menu are:
Home
Portfolio
Product Specs
Testimonials
Our Process
Contact
Some designs we like are:
http://www.tovenquarnsheds.example/
http://www.qzrsheds.example/
http://pannowsheds.example/
http://wistenhalls.example/
Not much requirements other than that so feel free to be creative!
Updates
Target Market(s)
Construction
Commercial and Residential Buildings
Industry/Entity Type
Construction Company
Number of Pages Required
5+ page
Look and feel

```html
<!DOCTYPE html>
<html lang="en">
<head>
<meta charset="utf-8">
<title>Brindle Structures</title>
<link rel="stylesheet" href="https://fonts.googleapis.com/css2?family=Open+Sans:ital,wght@0,400;0,600;0,700;1,400&family=Dancing+Script:wght@600&display=swap">
<style>
:root{
  --red:#d3271c;
  --red-dark:#b81f16;
  --blue:#1aa1dc;
  --link-blue:#2aa4d8;
  --ink:#222;
  --grey:#6a6a6a;
  --pale:#f3f3f3;
  --footer:#302c2b;
  --footer-line:#4a4544;
  --black:#111;
  --white:#fff;
}
*{box-sizing:border-box;margin:0;padding:0}
html,body{width:1200px;height:3279px;overflow:hidden}
body{position:relative;background:var(--white);font-family:"Open Sans",Arial,sans-serif;color:var(--ink)}
.abs{position:absolute}

/* header */
.site-header{position:absolute;left:0;top:0;width:1200px;height:92px;background:var(--black)}
.header-band{position:absolute;left:0;top:0}
.brand{position:absolute;left:80px;top:22px;display:flex;align-items:center;gap:10px;font-size:30px;font-weight:700;color:var(--link-blue)}
.brand-mark{width:18px;height:18px;background:var(--red);border-radius:50%}
.main-nav{position:absolute;right:36px;top:34px;display:flex;gap:22px;font-size:16px;color:var(--white);text-transform:uppercase}
.main-nav .active{border-bottom:2px solid var(--white)}

/* hero */
.hero{position:absolute;left:0;top:92px;width:1200px;height:548px;
  background:linear-gradient(180deg,#7fb2de 0%,#b9d3ea 22%,#6e6a66 30%,#807a74 62%,#5d7d3a 82%,#8aa55a 100%)}
.hero-title{position:absolute;left:0;width:1200px;top:198px;text-align:center;font-family:"Dancing Script",cursive;font-size:50px;color:#9fe3f0}

/* welcome */
.section-title{position:absolute;left:0;width:1200px;text-align:center;font-size:28px;color:var(--red);text-transform:uppercase;font-weight:400}
.welcome-rule{position:absolute;left:380px;top:738px;width:440px;height:1px;background:#ddd}
.welcome-text{position:absolute;left:96px;top:758px;width:1010px;text-align:center;font-size:12.5px;line-height:19px;font-style:italic;color:#444}

/* services */
.services{position:absolute;left:0;top:918px;width:1200px;height:562px;background:var(--pale)}
.services-intro{position:absolute;left:90px;top:1022px;width:1020px;text-align:center;font-size:13px;line-height:22px;color:#555}
.service{position:absolute;top:1104px;width:240px}
.service-photo{width:240px;height:190px;border:2px solid var(--link-blue)}
.service-name{margin-top:38px;font-size:15px;color:var(--link-blue);text-transform:uppercase}
.service-text{margin-top:22px;font-size:13px;line-height:19px;color:var(--grey)}

/* portfolio */
.portfolio-rule{position:absolute;top:1548px;height:3px;width:240px;background:#777}
.portfolio-dot{position:absolute;top:1543px;width:22px;height:13px;border-radius:50%;background:var(--red)}
.filters{position:absolute;left:80px;top:1596px;width:1040px;display:flex;justify-content:space-between;font-size:14px;color:var(--ink)}
.filter{display:flex;align-items:center;gap:8px}
.filter svg{width:26px;height:26px}
.portfolio-photo{position:absolute;left:264px;top:1727px;width:672px;height:393px;
  background:linear-gradient(180deg,#a9c8e8 0%,#e2e8ee 35%,#b8b8b4 55%,#4f8a32 78%,#3e7a27 100%)}

/* info band */
.info-band{position:absolute;left:0;top:2197px;width:1200px;height:415px}
.info-col{position:absolute;top:0;height:415px}
.info-col.red{background:var(--red)}
.info-col.blue{background:var(--blue)}
.info-heading{position:absolute;left:0;width:100%;top:38px;text-align:center;color:var(--white);font-size:15px;text-transform:uppercase}
.info-item{position:absolute;display:flex;align-items:flex-start;gap:20px;color:var(--white);font-size:12.5px;line-height:18px}
.info-icon{flex:none;width:48px;height:40px;border-radius:50%;background:var(--link-blue);border:2px solid #0d5f8a;display:flex;align-items:center;justify-content:center}
.features .info-icon{background:#1b5b8c;border-color:#0e3a5c}
.portrait{position:absolute;left:533px;top:2281px;width:132px;height:132px;border-radius:50%;border:4px solid #fff;background:radial-gradient(circle at 50% 40%,#c8a58c 0%,#6b5a52 55%,#2e3442 100%)}
.t-arrow{position:absolute;top:2339px;width:18px;height:18px;border:1px solid #222;background:#fff;display:flex;align-items:center;justify-content:center}
.quote{position:absolute;left:466px;top:2432px;width:268px;text-align:center;font-size:12px;line-height:17px;color:#fff;font-style:italic}
.quote-mark{position:absolute;top:2422px;font-size:36px;font-weight:700;color:#111;line-height:1}
.t-name{position:absolute;left:426px;width:348px;top:2497px;text-align:center;font-size:12px;color:#111}
.t-place{position:absolute;left:426px;width:348px;top:2516px;text-align:center;font-size:12px;color:#111}
.read-more{position:absolute;left:555px;top:2546px;width:90px;height:30px;border:2px solid #1a1a1a;border-radius:6px;color:#fff;font-size:12px;display:flex;align-items:center;justify-content:center}

/* call */
.call-photo{position:absolute;left:273px;top:2634px;width:262px;height:295px;background:linear-gradient(180deg,#eef1f3 0%,#cbd7e2 40%,#a8c0d8 100%)}
.call-now{position:absolute;left:651px;top:2712px;font-size:33px;color:var(--red);line-height:1}
.call-line{position:absolute;left:651px;font-size:22px;color:var(--link-blue);line-height:1}
.call-phone{position:absolute;left:651px;top:2815px;font-size:33px;color:#111;line-height:1}

/* footer */
.site-footer{position:absolute;left:0;top:2929px;width:1200px;height:302px;background:var(--footer);color:#ddd;font-size:12px}
.f-head{position:absolute;top:26px;font-size:14px;font-weight:600;color:var(--link-blue)}
.f-head-rule{position:absolute;top:52px;height:1px;background:var(--footer-line)}
.f-nav{position:absolute;left:81px;top:66px;width:154px;list-style:none}
.f-nav li{height:32px;line-height:30px;border-bottom:1px solid var(--footer-line);padding-left:8px}
.news-photo{position:absolute;left:273px;top:71px;width:123px;height:148px;background:linear-gradient(180deg,#9ab4cf 0%,#5b5f64 50%,#3b3a38 100%);border:2px solid #888}
.news-side{position:absolute;left:406px;top:68px;width:126px;font-size:12px;line-height:17px;text-align:justify}
.news-below{position:absolute;left:273px;top:225px;width:259px;font-size:12px;line-height:17px}
.loc-row{position:absolute;left:577px;display:flex;gap:10px;align-items:flex-start;line-height:16px}
.map{position:absolute;left:577px;top:173px;width:236px;height:107px;border:3px solid #777;background:linear-gradient(135deg,#e6e1d3 0%,#d9d6cc 50%,#c9d8c3 100%)}
.nl-text{position:absolute;left:863px;top:64px;width:250px;font-size:11.5px;line-height:16px}
.nl-field{position:absolute;left:863px;top:101px;width:243px;height:26px;background:#fff;border-radius:3px;color:#888;font-size:11px;padding:6px 8px}
.nl-button{position:absolute;left:1036px;top:104px;width:66px;height:20px;background:var(--link-blue);color:#fff;font-size:11px;display:flex;align-items:center;justify-content:center;border-radius:2px}
.social{position:absolute;top:138px;width:26px;height:26px;border-radius:3px}
.copyright{position:absolute;left:0;top:3231px;width:1200px;height:48px;background:#141212;color:#999;font-size:11px;text-align:center;line-height:48px}
</style>
</head>
<body>

<header class="site-header">
  <svg class="header-band" width="1200" height="92" viewBox="0 0 1200 92"><polygon points="470,0 1200,0 1200,92 430,92" fill="#d3271c"/></svg>
  <div class="brand"><span class="brand-mark"></span>Brindle Structures</div>
  <nav class="main-nav">
    <span class="active">Home</span><span>Portfolio</span><span>Products</span><span>Testimonials</span><span>Our Process</span><span>Contact</span>
  </nav>
</header>

<section class="hero" role="img" aria-label="Photo of a two-storey stone house with double garage under a blue sky">
  <h1 class="hero-title">Building Dreams,So You Can Build Dreams</h1>
</section>

<h2 class="section-title" style="top:700px">Welcome to Brindle Structures</h2>
<div class="welcome-rule"></div>
<p class="welcome-text">Lorem ipsum dolor sit amet, consectetur adipiscing elit. Nunc quis massa nec quam mollis pellentesque. Donec sagittis tristique nunc. Vestibulum id nulla vel mauris suscipit tincidunt in vel tortor. Donec fermentum tempor sollicitudin. Nulla quis urna tincidunt, sagittis leo et, laoreet odio. Quisque commodo pretium lacus, molestie egestas urna vulputate non. Nam massa elit, accumsan eu massa commodo, aliquam malesuada turpis. Duis malesuada euismod augue eu placerat. Nulla pulvinar tempor arcu, in pulvinar erat euismod in. Vestibulum non nunc at ante eleifend pellentesque. Nullam consectetur, magna id aliquam semper, nibh augue mattis est, vel egestas justo magna vitae nulla. Duis ornare vel mauris sit amet consectetur.</p>

<section class="services"></section>
<h2 class="section-title" style="top:964px">Our Services</h2>
<p class="services-intro">Lorem Ipsum dolor sit amet, consectetur adipiscing elit. Praesent rutrum sem quam, vel dignissim lacus placerat quis. Nunc et turpis nec massa vulputate efficitur ut Proin accumsan at massa eget dapibus. Ut sollicitudin id est non auctor. Praesent ut tincidunt elit.</p>

<div class="service" style="left:81px">
  <div class="service-photo" role="img" aria-label="Photo of two engineers in hard hats reviewing plans on site" style="background:linear-gradient(160deg,#8fb0c8 0%,#5c7188 50%,#2f3d52 100%)"></div>
  <div class="service-name">General Contracting</div>
  <p class="service-text">Construction Department Specializing in Commercial Remodeling and Maintenance.</p>
</div>
<div class="service" style="left:347px">
  <div class="service-photo" role="img" aria-label="Photo of builders working on a timber frame" style="background:linear-gradient(160deg,#e2b894 0%,#b9754a 55%,#6d3f25 100%)"></div>
  <div class="service-name">Construction</div>
  <p class="service-text">Brindle Structures has spent a century refining our construction and safety practices.</p>
</div>
<div class="service" style="left:613px">
  <div class="service-photo" role="img" aria-label="Photo of a technician laying floor tiles" style="background:linear-gradient(160deg,#8a8580 0%,#b7875a 55%,#5a4a3c 100%)"></div>
  <div class="service-name">Commercial Maintenance</div>
  <p class="service-text">Brindle Structures has skilled technicians ready to repair and maintain commercial facilities.</p>
</div>
<div class="service" style="left:880px">
  <div class="service-photo" role="img" aria-label="Photo of a painter rolling paint onto a wall" style="background:linear-gradient(160deg,#e7f0ee 0%,#9fd6c6 50%,#5f8fa8 100%)"></div>
  <div class="service-name">Painting</div>
  <p class="service-text">Our Painting Division is staffed with professional painters who have lots of experience in the field of projects.</p>
</div>

<div class="portfolio-rule" style="left:243px"></div>
<div class="portfolio-dot" style="left:463px"></div>
<h2 class="section-title" style="top:1530px">Our Portfolio</h2>
<div class="portfolio-dot" style="left:715px"></div>
<div class="portfolio-rule" style="left:717px"></div>

<div class="filters">
  <span class="filter"><svg viewBox="0 0 26 26"><rect x="2" y="6" width="22" height="3" fill="#d3271c"/><rect x="2" y="12" width="22" height="3" fill="#d3271c"/><rect x="2" y="18" width="22" height="3" fill="#d3271c"/></svg>Show All</span>
  <span class="filter"><svg viewBox="0 0 26 26"><rect x="3" y="5" width="20" height="18" fill="#fff" stroke="#2a9a3a" stroke-width="2"/><rect x="11" y="8" width="4" height="12" fill="#d3271c"/><rect x="7" y="12" width="12" height="4" fill="#d3271c"/></svg>Hospitals</span>
  <span class="filter"><svg viewBox="0 0 26 26"><polygon points="13,3 24,11 2,11" fill="#2a9a3a"/><rect x="4" y="11" width="18" height="12" fill="#2a9a3a"/><rect x="11" y="16" width="4" height="7" fill="#fff"/></svg>Schools</span>
  <span class="filter"><svg viewBox="0 0 26 26"><polygon points="13,3 25,13 1,13" fill="#1b7fd1"/><rect x="5" y="13" width="16" height="10" fill="#1b7fd1"/></svg>Houses</span>
  <span class="filter"><svg viewBox="0 0 26 26"><rect x="8" y="2" width="10" height="22" fill="#8cc4ea" stroke="#3b86c2"/><rect x="4" y="10" width="6" height="14" fill="#b9dcf3" stroke="#3b86c2"/></svg>Flats</span>
  <span class="filter"><svg viewBox="0 0 26 26"><rect x="10" y="2" width="10" height="22" fill="#ddd" stroke="#888"/><rect x="4" y="9" width="8" height="15" fill="#eee" stroke="#888"/></svg>Offices</span>
  <span class="filter"><svg viewBox="0 0 26 26"><polygon points="13,2 25,8 1,8" fill="#1e3f73"/><rect x="3" y="10" width="3" height="11" fill="#1e3f73"/><rect x="9" y="10" width="3" height="11" fill="#1e3f73"/><rect x="14" y="10" width="3" height="11" fill="#1e3f73"/><rect x="20" y="10" width="3" height="11" fill="#1e3f73"/><rect x="1" y="22" width="24" height="3" fill="#1e3f73"/></svg>Universities</span>
</div>

<svg class="abs" style="left:228px;top:1672px" width="744" height="474" viewBox="0 0 744 474">
  <path d="M4 14 H250 Q262 14 268 4 H476 Q482 14 494 14 H740 V470 H4 Z" fill="#fff" stroke="#d3271c" stroke-width="4"/>
  <circle cx="358" cy="28" r="12" fill="#1a7fd1"/>
  <path d="M361 22 L355 28 L361 34" fill="none" stroke="#fff" stroke-width="2.5"/>
  <circle cx="404" cy="28" r="12" fill="#1a7fd1"/>
  <path d="M401 22 L407 28 L401 34" fill="none" stroke="#fff" stroke-width="2.5"/>
</svg>
<div class="portfolio-photo" role="img" aria-label="Photo of a modern grey two-storey house with a large lawn"></div>

<section class="info-band">
  <div class="info-col red" style="left:0;width:426px">
    <h3 class="info-heading">How our Keystone property service works:</h3>
  </div>
  <div class="info-col blue" style="left:426px;width:348px">
    <h3 class="info-heading">Testimonial</h3>
  </div>
  <div class="info-col red features" style="left:774px;width:426px">
    <h3 class="info-heading">Features</h3>
  </div>
</section>

<div class="info-item" style="left:82px;top:2296px;width:320px">
  <span class="info-icon"><svg width="24" height="24" viewBox="0 0 24 24"><circle cx="12" cy="6" r="4" fill="#111"/><rect x="6" y="11" width="12" height="11" rx="3" fill="#111"/></svg></span>
  <span>Our home owners show us what work they require to be done.</span>
</div>
<div class="info-item" style="left:82px;top:2388px;width:320px">
  <span class="info-icon"><svg width="24" height="24" viewBox="0 0 24 24"><rect x="3" y="4" width="18" height="13" fill="none" stroke="#111" stroke-width="2"/><rect x="9" y="18" width="6" height="3" fill="#111"/></svg></span>
  <span>We then offer our clients a choice of guaranteed "Keystone SOLUTIONS".</span>
</div>
<div class="info-item" style="left:82px;top:2480px;width:320px">
  <span class="info-icon"><svg width="24" height="24" viewBox="0 0 24 24"><circle cx="7" cy="7" r="3" fill="#111"/><circle cx="17" cy="7" r="3" fill="#111"/><rect x="3" y="11" width="8" height="9" rx="2" fill="#111"/><rect x="13" y="11" width="8" height="9" rx="2" fill="#111"/></svg></span>
  <span>Once approved by our customers, the people at Keystone Property Services then take FULL responsibility to complete the works.</span>
</div>

<div class="portrait" role="img" aria-label="Portrait photo of a client in a suit"></div>
<span class="t-arrow" style="left:453px"><svg width="10" height="10" viewBox="0 0 10 10"><path d="M7 1 L3 5 L7 9" fill="none" stroke="#222" stroke-width="1.5"/></svg></span>
<span class="t-arrow" style="left:727px"><svg width="10" height="10" viewBox="0 0 10 10"><path d="M3 1 L7 5 L3 9" fill="none" stroke="#222" stroke-width="1.5"/></svg></span>
<span class="quote-mark" style="left:448px">&ldquo;</span>
<p class="quote">It is a long established fact that a reader will be distracted by the readable content of a page when looking at its layout. The point of using Lorem.</p>
<span class="quote-mark" style="left:732px">&rdquo;</span>
<div class="t-name">Marla Voss</div>
<div class="t-place">Cedar Falls, IA</div>
<div class="read-more">Read More</div>

<div class="info-item features" style="left:806px;top:2296px;width:330px">
  <span class="info-icon"><svg width="24" height="24" viewBox="0 0 24 24"><path d="M4 20 L18 6 L21 9 L7 23 Z" fill="#111"/></svg></span>
  <span>indoor, outdoor, big &amp; small we deal with every job with the exact same professionism and pride.</span>
</div>
<div class="info-item features" style="left:806px;top:2388px;width:330px">
  <span class="info-icon"><svg width="24" height="24" viewBox="0 0 24 24"><path d="M14 2 L5 13 H11 L9 22 L19 10 H13 Z" fill="#111"/></svg></span>
  <span>We have specialist teams with over 20yrs experience that can handle any job anytime.</span>
</div>
<div class="info-item features" style="left:806px;top:2480px;width:330px">
  <span class="info-icon"><svg width="24" height="24" viewBox="0 0 24 24"><rect x="3" y="4" width="14" height="6" fill="#111"/><rect x="10" y="9" width="4" height="13" fill="#111"/></svg></span>
  <span>We work 7 days a week &amp; support our client on whole week.</span>
</div>

<div class="call-photo" role="img" aria-label="Photo of a smiling project manager in a white hard hat holding a clipboard"></div>
<div class="call-now">CALL NOW!</div>
<div class="call-line" style="top:2755px">&amp; Speak Directly</div>
<div class="call-line" style="top:2786px">to one of our Project Managers</div>
<div class="call-phone">0800 555 0199</div>

<footer class="site-footer">
  <h4 class="f-head" style="left:81px">Navigation</h4>
  <div class="f-head-rule" style="left:81px;width:154px"></div>
  <ul class="f-nav">
    <li>Home</li><li>About</li><li>Services</li><li>Portfolio</li><li>Basalt Family</li><li>Testimonial</li><li>Contact</li>
  </ul>

  <h4 class="f-head" style="left:273px">News &amp; Updates</h4>
  <div class="f-head-rule" style="left:273px;width:259px"></div>
  <div class="news-photo" role="img" aria-label="Photo of a newly built house at dusk"></div>
  <p class="news-side">Lorem ipsum dolor sit amet, consectetur adipiscing elit. Fusce convallis libero quis felistor malesuada. Nam ultrices et velit sed maximus.</p>
  <p class="news-below">Mauris ante nisl, facilisis vel condimentum id, tristique at mauris. Donec ex nisi, lacinia non efficitur id, scelerisque id dolor. Vivamus euismod velit eget velit iaculis placerat.</p>

  <h4 class="f-head" style="left:577px">Our Location</h4>
  <div class="f-head-rule" style="left:577px;width:236px"></div>
  <div class="loc-row" style="top:68px"><svg width="12" height="16" viewBox="0 0 12 16"><path d="M6 0 C2.7 0 0 2.6 0 6 C0 10 6 16 6 16 C6 16 12 10 12 6 C12 2.6 9.3 0 6 0 Z" fill="#fff"/><circle cx="6" cy="6" r="2.2" fill="#302c2b"/></svg><span>Address Address Address Address<br>Address Address Address</span></div>
  <div class="loc-row" style="top:110px;font-size:16px"><svg width="14" height="16" viewBox="0 0 14 16"><path d="M3 1 L6 4 L4 7 C5 10 7 12 9 12 L11 10 L14 13 L11 16 C5 15 0 9 0 4 Z" fill="#fff"/></svg><span>800 555 0142</span></div>
  <div class="loc-row" style="top:143px;font-size:11.5px"><svg width="14" height="12" viewBox="0 0 14 12"><rect x="0" y="1" width="14" height="10" fill="#fff"/><path d="M0 1 L7 7 L14 1" fill="none" stroke="#302c2b" stroke-width="1.2"/></svg><span>info@brindlestructures.example</span></div>
  <div class="map" role="img" aria-label="Street map showing the office location"></div>

  <h4 class="f-head" style="left:863px">Newsletter Signup</h4>
  <div class="f-head-rule" style="left:863px;width:256px"></div>
  <p class="nl-text">Please enter your email address below to receive our FREE newsletter</p>
  <div class="nl-field">Your Email ID</div>
  <div class="nl-button">Subscribe</div>
  <span class="social" style="left:956px;background:#3aa6dd"></span>
  <span class="social" style="left:990px;background:#f07c23"></span>
  <span class="social" style="left:1024px;background:#3b5998"></span>
  <span class="social" style="left:1058px;background:#d8271c"></span>
</footer>
<div class="copyright">Copyright 2015 @brindlestructures.example. All rights reserved</div>

</body>
</html>
```